Brixo Tidy Yard Website

We need a website design for this new company. I've attached the company logo. This company is in the construction industry that provides general labor, maintenance and cleaning for construction sites. We want a clean and simple website that can be easy to navigate.

Target Market(s)

Construction industry

Industry/Entity Type

Construction

Number of Pages Required

2 page

Font styles to use
Sans Serif

```html
<!DOCTYPE html>
<html lang="en">
<head>
<meta charset="utf-8">
<title>Brixo Tidy Yard</title>
<link rel="stylesheet" href="https://fonts.googleapis.com/css2?family=Montserrat:wght@500;600;700&family=Rubik:wght@400;500&display=swap">
<style>
:root{
  --navy:#0a0a6b;
  --orange:#ff6a00;
  --ink:#1c1c2a;
  --muted:#6c6c7a;
  --band:#f5f6fc;
  --canvas:#f3f3f6;
  --line:#e4e4ec;
  --black:#050505;
  --white:#ffffff;
}
*{box-sizing:border-box;margin:0;padding:0}
html,body{width:1200px;height:3593px;overflow:hidden;background:var(--canvas);font-family:'Rubik',Arial,sans-serif;color:var(--ink)}
.page{position:absolute;left:148px;top:72px;width:964px;height:3431px;background:var(--white);box-shadow:0 6px 40px rgba(20,20,60,.12);overflow:hidden}
.abs{position:absolute}
.btn{position:absolute;display:flex;align-items:center;justify-content:center;font-family:'Montserrat',sans-serif;font-weight:600;font-size:10px;letter-spacing:.3px;color:var(--white);text-transform:uppercase}
.btn-orange{background:var(--orange)}
.btn-navy{background:var(--navy)}
/* top bar */
.topbar{left:0;top:0;width:964px;height:28px;background:var(--navy);color:var(--white);font-size:9px;display:flex;align-items:center;padding:0 38px}
.topbar .contact{display:flex;gap:26px}
.topbar .social{margin-left:auto;display:flex;gap:14px}
.social-dot{width:9px;height:9px;border:1.5px solid var(--white);border-radius:2px}
.navrow{left:0;top:28px;width:964px;height:48px;display:flex;align-items:center;padding:0 38px}
.brand{font-family:'Montserrat',sans-serif;font-weight:700;font-size:20px;color:var(--navy);display:flex;align-items:center;gap:6px}
.brand-mark{width:12px;height:12px;background:var(--orange)}
.mainnav{margin-left:auto;display:flex;gap:30px;font-size:11px;font-family:'Montserrat',sans-serif;font-weight:500}
.mainnav .active{border-bottom:2px solid var(--orange);padding-bottom:4px;font-weight:700}
.subrow{left:0;top:76px;width:964px;height:38px;background:var(--band);display:flex;align-items:center;padding-right:38px}
.subrow .search{margin-left:160px;font-size:10px;color:var(--muted);display:flex;align-items:center;gap:8px}
.subnav{margin-left:auto;display:flex;gap:26px;font-size:10px;font-family:'Montserrat',sans-serif;font-weight:600}
/* hero */
.hero-photo{left:0;top:114px;width:964px;height:330px;background:linear-gradient(120deg,#3b3b3f,#6b6b70 45%,#2f2f33)}
.hero-title{left:38px;top:200px;color:var(--white);font-family:'Montserrat',sans-serif;font-weight:700;font-size:24px}
.hero-sub{left:38px;top:232px;color:var(--white);font-size:17px}
.hero-dots{left:10px;top:278px;display:flex;flex-direction:column;gap:8px}
.hero-dots span{width:6px;height:6px;border:1px solid var(--white);border-radius:50%}
.quote-form{left:599px;top:148px;width:255px;height:305px;background:var(--white);box-shadow:0 4px 18px rgba(0,0,0,.15);padding:12px 18px}
.quote-form h3{font-family:'Montserrat',sans-serif;font-size:12px;font-weight:700;margin-bottom:10px}
.field{height:22px;border:1px solid var(--line);font-size:7px;color:#a0a0ae;padding:0 8px;display:flex;align-items:center;justify-content:space-between;margin-bottom:10px}
.field.area{height:62px;align-items:flex-start;padding-top:6px}
/* section headings */
.h2{font-family:'Montserrat',sans-serif;font-weight:500;font-size:24px;color:var(--ink)}
.accent{width:28px;height:3px;background:var(--orange)}
.body{font-size:11px;line-height:1.65;color:#3a3a4c}
.need-item{position:absolute;width:70px;text-align:center;font-size:11px;color:var(--ink)}
.need-icon{width:56px;height:56px;border:2px solid var(--orange);border-radius:50%;margin:0 auto 8px;display:flex;align-items:center;justify-content:center}
.band{left:0;width:964px;background:var(--band)}
.feature{position:absolute;width:200px;text-align:center}
.feature h4{font-family:'Montserrat',sans-serif;font-weight:700;font-size:12px;margin:12px 0 4px}
.feature p{font-size:10px;line-height:1.5;color:#3a3a4c}
/* cards */
.card{position:absolute;width:272px;background:var(--white);border:1px solid var(--line)}
.card-photo{height:124px}
.card-meta{display:flex;justify-content:space-between;font-size:7px;color:var(--muted);padding:8px 12px 4px}
.card h5{font-family:'Montserrat',sans-serif;font-weight:600;font-size:13px;padding:0 12px 6px}
.card p{font-size:8px;line-height:1.55;color:var(--muted);padding:0 12px 12px}
.arrow{position:absolute;width:34px;height:34px;border-radius:50%;display:flex;align-items:center;justify-content:center}
.arrow-light{background:#e3e3ea}
.arrow-orange{background:var(--orange)}
.dots{position:absolute;display:flex;gap:12px}
.dots span{width:11px;height:11px;border-radius:50%;background:#dcdce4}
.dots .on{background:var(--navy)}
.feature-h{font-family:'Montserrat',sans-serif;font-weight:700;font-size:22px;line-height:1.25;color:var(--ink)}
.dark-banner{left:33px;top:2290px;width:931px;height:203px;background:linear-gradient(90deg,#1f1f22,#38383c 55%,#27272a)}
.tcard{position:absolute;width:272px;height:196px;background:var(--white);box-shadow:0 2px 14px rgba(0,0,0,.08);padding:16px 14px}
.stars{display:flex;gap:3px;justify-content:center;margin-bottom:28px}
.tcard p{font-size:8px;line-height:1.55;color:#3a3a4c}
.tfoot{position:absolute;left:14px;right:14px;bottom:14px;display:flex;align-items:center;font-size:7.5px;color:var(--muted)}
.avatar{width:22px;height:22px;border-radius:50%;background:#c9b8a6;margin-right:8px}
/* footer */
.footer{left:0;top:2880px;width:964px;height:551px;background:var(--black);color:var(--white)}
.col h6{font-family:'Montserrat',sans-serif;font-size:9px;font-weight:700;padding-bottom:8px;border-bottom:1px solid #666;width:70px;margin-bottom:10px}
.col ul{list-style:none;font-size:8px;line-height:1.9;color:#ddd}
.col{position:absolute}
.sq{width:34px;height:34px;border:1px solid #ccc;display:flex;align-items:center;justify-content:center}
.sq span{width:10px;height:10px;background:var(--white)}
</style>
</head>
<body>
<div class="page">
  <div class="abs topbar">
    <div class="contact"><span>☏ 555-014-2290</span><span>✉ hello@brixotidy.com</span></div>
    <div class="social"><span class="social-dot"></span><span class="social-dot"></span><span class="social-dot"></span></div>
  </div>
  <div class="abs navrow">
    <div class="brand"><span class="brand-mark"></span>Brixo</div>
    <nav class="mainnav"><span class="active">Home</span><span>About Us</span><span>Services ▾</span><span>Contact us</span></nav>
  </div>
  <div class="abs subrow">
    <div class="btn btn-orange" style="left:38px;top:0;width:120px;height:38px">Get a Quote</div>
    <div class="search"><svg width="11" height="11" viewBox="0 0 11 11"><circle cx="4.5" cy="4.5" r="3.5" fill="none" stroke="#333" stroke-width="1.4"/><line x1="7" y1="7" x2="10" y2="10" stroke="#333" stroke-width="1.4"/></svg>Search</div>
    <nav class="subnav"><span>Our Blog</span><span>Promotions ▾</span><span>Pricing</span><span>Claims</span></nav>
  </div>

  <div class="abs hero-photo" role="img" aria-label="Aerial view of a building construction site"></div>
  <svg class="abs" style="left:0;top:400px" width="964" height="100" viewBox="0 0 964 100"><path d="M0 20 C250 60 600 70 964 10 L964 100 L0 100Z" fill="var(--orange)"/><path d="M0 50 C300 80 650 90 964 55 L964 100 L0 100Z" fill="var(--white)"/></svg>
  <div class="abs hero-title">We help you</div>
  <div class="abs hero-sub">Focusing on Your Construction</div>
  <div class="abs hero-dots"><span></span><span></span><span></span></div>
  <div class="btn btn-orange" style="left:38px;top:283px;width:140px;height:40px">View Our Cases</div>
  <div class="btn btn-navy" style="left:192px;top:283px;width:140px;height:40px">View Our Services</div>
  <div class="abs quote-form">
    <h3>Get a Quote Now</h3>
    <div class="field">Your full name</div>
    <div class="field">Your email</div>
    <div class="field">Service required <span>▾</span></div>
    <div class="field">Construction site location <span>▾</span></div>
    <div class="field area">Tell us about your site needs</div>
    <div class="btn btn-orange" style="left:18px;top:256px;width:219px;height:30px">Enquire</div>
  </div>

  <div class="abs h2" style="left:33px;top:565px">Get your need for the best price</div>
  <div class="need-item" style="left:26px;top:628px"><div class="need-icon"><svg width="26" height="26" viewBox="0 0 26 26" fill="none" stroke="var(--orange)" stroke-width="1.6"><circle cx="13" cy="8" r="5"/><path d="M3 24c0-6 4-9 10-9s10 3 10 9"/></svg></div>Labor</div>
  <div class="need-item" style="left:105px;top:628px"><div class="need-icon"><svg width="26" height="26" viewBox="0 0 26 26" fill="none" stroke="var(--orange)" stroke-width="1.6"><path d="M5 21 L15 11"/><circle cx="18" cy="8" r="5"/><circle cx="5" cy="21" r="2"/></svg></div>Maintenance</div>
  <div class="need-item" style="left:184px;top:628px"><div class="need-icon"><svg width="26" height="26" viewBox="0 0 26 26" fill="none" stroke="var(--orange)" stroke-width="1.6"><rect x="5" y="9" width="16" height="14"/><path d="M9 9V5h8v4M5 15h16"/></svg></div>Cleaning</div>
  <p class="abs body" style="left:389px;top:626px;width:470px">Brixo Tidy Yard keeps your build moving with skilled labor, reliable site upkeep and a thorough cleanup after every phase. Tell us what your site needs and we will match the right crew at a fair price, fast.</p>

  <div class="abs band" style="top:763px;height:405px"></div>
  <svg class="abs" style="left:0;top:1150px" width="964" height="40" viewBox="0 0 964 40"><path d="M0 0 L964 0 L964 15 C600 40 300 30 0 10Z" fill="var(--band)"/></svg>
  <div class="feature" style="left:130px;top:800px">
    <svg width="100" height="100" viewBox="0 0 100 100" fill="none" stroke="var(--navy)" stroke-width="1.6"><rect x="20" y="20" width="60" height="60" transform="rotate(45 50 50)"/><circle cx="50" cy="50" r="14"/><path d="M50 42v8l6 4"/></svg>
    <h4>EFFICIENCY</h4><p>We've made the process as simple as possible; it only takes you 2 minutes to complete the form.</p>
  </div>
  <div class="feature" style="left:382px;top:770px">
    <svg width="100" height="100" viewBox="0 0 100 100" fill="none" stroke="var(--navy)" stroke-width="1.6"><rect x="20" y="20" width="60" height="60" transform="rotate(45 50 50)"/><path d="M36 40h28L50 62Z"/><path d="M50 40v22"/></svg>
    <h4>CAPACITY</h4><p>We provide the capability to service all types of services, general labor, maintenance and cleaning.</p>
  </div>
  <div class="feature" style="left:636px;top:800px">
    <svg width="100" height="100" viewBox="0 0 100 100" fill="none" stroke="var(--navy)" stroke-width="1.6"><rect x="20" y="20" width="60" height="60" transform="rotate(45 50 50)"/><circle cx="50" cy="50" r="7"/><circle cx="50" cy="50" r="14" stroke-dasharray="5 3"/></svg>
    <h4>CUSTOMIZED</h4><p>We provide a variety of services for your site and you are free to choose what you want.</p>
  </div>
  <div class="btn btn-navy" style="left:382px;top:1084px;width:140px;height:38px">Get a Quote</div>

  <div class="abs h2" style="left:33px;top:1205px;display:flex;align-items:center;gap:8px">Our Cases <svg width="18" height="18" viewBox="0 0 18 18" fill="none" stroke="var(--ink)" stroke-width="1.4"><circle cx="9" cy="9" r="7"/><path d="M6 9h6M10 6.5 12.5 9 10 11.5"/></svg></div>
  <div class="arrow arrow-light" style="left:-8px;top:1383px"><svg width="10" height="10" viewBox="0 0 10 10"><path d="M7 1 3 5l4 4" fill="none" stroke="#555" stroke-width="1.5"/></svg></div>
  <div class="card" style="left:33px;top:1264px"><div class="card-photo" role="img" aria-label="Worker cutting timber with a mitre saw" style="background:linear-gradient(135deg,#c9c2b8,#8a8176)"></div><div class="card-meta"><span>Client Name</span><span>DEC 20</span></div><h5>Case Title</h5><p>Full site cleanup after framing works, debris removal and a final sweep before handover to the owner.</p></div>
  <div class="card" style="left:315px;top:1264px"><div class="card-photo" role="img" aria-label="Worker in safety vest among steel scaffolding" style="background:linear-gradient(135deg,#9aa3aa,#5c646b)"></div><div class="card-meta"><span>Client Name</span><span>DEC 20</span></div><h5>Case Title</h5><p>Scaffold upkeep and general labor crew supplied for a four week commercial build downtown.</p></div>
  <div class="card" style="left:597px;top:1264px"><div class="card-photo" role="img" aria-label="Steel rebar mesh on a concrete slab" style="background:linear-gradient(135deg,#55585c,#2e3033)"></div><div class="card-meta"><span>Client Name</span><span>DEC 20</span></div><h5>Case Title</h5><p>Rebar area prepared, cleared and kept tidy through every pour on a residential project.</p></div>
  <div class="arrow arrow-orange" style="left:880px;top:1383px"><svg width="10" height="10" viewBox="0 0 10 10"><path d="M3 1l4 4-4 4" fill="none" stroke="#fff" stroke-width="1.5"/></svg></div>
  <div class="dots" style="left:450px;top:1555px"><span class="on"></span><span></span></div>

  <div class="abs band" style="top:1598px;height:895px"></div>
  <div class="abs" role="img" aria-label="Row of yellow hard hats hanging on an orange container" style="left:33px;top:1651px;width:391px;height:257px;background:linear-gradient(135deg,#d8e2ea,#e08a3c 55%,#b94f1f)"></div>
  <div class="abs accent" style="left:458px;top:1652px"></div>
  <div class="abs feature-h" style="left:458px;top:1664px;width:360px">We Got a large number of general labor</div>
  <p class="abs body" style="left:458px;top:1744px;width:400px">Our crews are trained, insured and ready to join your site on short notice. From loading and hauling to site prep, we bring steady hands for every phase of your build.</p>
  <div class="btn btn-orange" style="left:458px;top:1842px;width:128px;height:38px">Get a Quote</div>

  <div class="abs accent" style="left:33px;top:1963px"></div>
  <div class="abs feature-h" style="left:33px;top:1975px;width:400px">We got different services and plans for you</div>
  <p class="abs body" style="left:33px;top:2045px;width:410px">Pick a single cleanup or a monthly plan that covers labor, repairs and site care. Every plan is shaped around your schedule, your crew size and your budget.</p>
  <div class="btn btn-navy" style="left:33px;top:2140px;width:140px;height:36px">View Services</div>
  <div class="btn btn-orange" style="left:185px;top:2140px;width:128px;height:36px">Get a Quote</div>
  <div class="abs" role="img" aria-label="Welder grinding metal with flying sparks" style="left:477px;top:1961px;width:391px;height:258px;background:linear-gradient(135deg,#1e2a36,#3b4b5a 50%,#a0622c)"></div>

  <div class="abs dark-banner" role="img" aria-label="Dark construction site at dusk"></div>
  <div class="abs accent" style="left:432px;top:2318px;background:var(--white)"></div>
  <div class="abs" style="left:432px;top:2330px;color:var(--white);font-family:'Montserrat',sans-serif;font-weight:700;font-size:17px">We help you focusing on the construction</div>
  <p class="abs" style="left:432px;top:2362px;width:470px;color:#e6e6e6;font-size:11px;line-height:1.6">Leave the cleanup, upkeep and extra hands to us, so your team can stay focused on building quality work on time.</p>
  <div class="btn btn-orange" style="left:432px;top:2414px;width:128px;height:36px">Get a Quote</div>

  <div class="abs accent" style="left:33px;top:2544px"></div>
  <div class="abs h2" style="left:33px;top:2560px;display:flex;align-items:center;gap:8px">see what customers are saying about us <svg width="18" height="18" viewBox="0 0 18 18" fill="none" stroke="var(--ink)" stroke-width="1.4"><circle cx="9" cy="9" r="7"/><path d="M6 9h6M10 6.5 12.5 9 10 11.5"/></svg></div>
  <div class="arrow arrow-light" style="left:-8px;top:2706px"><svg width="10" height="10" viewBox="0 0 10 10"><path d="M7 1 3 5l4 4" fill="none" stroke="#555" stroke-width="1.5"/></svg></div>
  <div class="tcard" style="left:33px;top:2624px"><div class="stars">★★★★★</div><p>The crew showed up on time, worked hard and left our site spotless. We will book them again.</p><div class="tfoot"><span class="avatar"></span>Mara Lindqvist<span style="margin-left:auto">DEC 20, 2019</span></div></div>
  <div class="tcard" style="left:315px;top:2624px"><div class="stars">★★★★★</div><p>Fast quotes, fair prices and great communication during the whole maintenance contract.</p><div class="tfoot"><span class="avatar" style="background:#3d4f5c"></span>Mara Lindqvist<span style="margin-left:auto">DEC 20, 2019</span></div></div>
  <div class="tcard" style="left:597px;top:2624px"><div class="stars">★★★★★</div><p>Easy to book and very thorough. Our final inspection went through without any issue.</p><div class="tfoot"><span class="avatar" style="background:#d8a98a"></span>Mara Lindqvist<span style="margin-left:auto">DEC 20, 2019</span></div></div>
  <div class="arrow arrow-orange" style="left:880px;top:2706px"><svg width="10" height="10" viewBox="0 0 10 10"><path d="M3 1l4 4-4 4" fill="none" stroke="#fff" stroke-width="1.5"/></svg></div>
  <div class="dots" style="left:450px;top:2840px"><span class="on"></span><span></span></div>

  <div class="abs footer">
    <svg class="abs" style="left:0;top:0" width="964" height="40" viewBox="0 0 964 40"><path d="M0 0H964V8C650 40 300 -5 0 25Z" fill="var(--white)"/></svg>
    <div class="abs" style="left:150px;top:96px;font-size:18px">Subscribe to our newfeed</div>
    <div class="abs" style="left:460px;top:88px;width:239px;height:36px;background:var(--white);color:var(--ink);font-size:8px;font-weight:500;display:flex;align-items:center;padding-left:10px">YOUR EMAIL</div>
    <div class="btn btn-orange" style="left:699px;top:88px;width:115px;height:36px">Subscribe Now</div>
    <div class="col" style="left:33px;top:220px"><h6>SITEMAP</h6><ul><li>HOME</li><li>ABOUT US</li><li>GENERAL LABOR</li><li>MAINTENANCE</li><li>CLEANING</li><li>PROMOTIONS</li><li>PRICING</li></ul></div>
    <div class="col" style="left:246px;top:220px"><h6>CLAIM INFO</h6><ul><li>CLAIM GUIDE</li><li>CLAIM FAQ</li></ul><h6 style="margin-top:16px">ABOUT US</h6><ul><li>ABOUT US</li><li>OUR TEAM</li><li>JOIN US</li><li>MEDIA</li></ul></div>
    <div class="col" style="left:456px;top:220px"><h6>HELP</h6><ul><li>TERMS</li><li>FAQ</li><li>CONTACT US</li><li>LOCATOR</li></ul><h6 style="margin-top:16px">BLOG</h6><ul><li>VIEW BLOG</li></ul></div>
    <div class="col" style="left:668px;top:220px"><h6>CONNECT</h6><div style="display:flex;gap:12px;margin-top:4px"><div class="sq"><span></span></div><div class="sq"><span></span></div><div class="sq"><span></span></div></div><div class="btn btn-orange" style="left:0;top:86px;width:128px;height:36px">Get a Quote</div></div>
    <div class="abs" style="left:0;top:528px;width:964px;text-align:center;font-size:8px;color:#ccc">© Copyright 2019 <b>Brixo Tidy Yard</b></div>
  </div>
</div>
</body>
</html>
```